3 in 1 website - Home Lens Studio Extra + Keeping Moments LLC + Marla's Game Shots

Help me simplify and organize my business life. I am a sports photographer (action, individual and teams), real estate photographer (stills and drones) and I transfer videos and photos to jump drives, along with photo restoration, etc. Currently, I have a functioning website for the transfer/restoration business at KeepingMomentsLLC.example which was recently created and I like it. I have received several really good ideas for the Real Estate Photography portion! I don't have anything started for the Sports Pics. My vision possibly includes a main/home page giving people the option to choose real estate, sports or transfer/restoration. I just want them combined into one site....somehow to better organize my businesses and give me ONE place to keep to updated and check for communication. I just updated the brief again and added logo files for my "parent" company called "Keeping Moments". I prefer this logo at the top of the main/home page, please. I previously uploaded the logo for Home Lens Studio Extra which would be used with the real estate portion of my business. At this point, I don't have a logo for the sports photography portion.

Target Market(s)

Real Estate Agents and Brokers; Sports team, parents and boosters; Community members typically 40+ years old

Industry/Entity Type

Real Estate Photography; Local sports teams; Community members 40+ years old

Coding

Coded - Design and coding required

Number of Pages Required

3 page

Requirements
Must have
• At least one page for each area: real estate, sports, digital transfers. The real estate will need to connect to an account I have with QNL for checkout options. The sports page(s) will need to connect to a 3rd party service, also. The digital transfers, photo restorations, etc. would just need a way for them to request service.
Nice to have
• I currently have a website at KeepingMomentsLLC.example for the digital transfer/photo restoration part of my business. I like this website but want it integrated with one main site for all 3 businesses.

```html
<!DOCTYPE html>
<html lang="en">
<head>
<meta charset="utf-8">
<title>Keeping Moments Photography</title>
<link rel="stylesheet" href="https://fonts.googleapis.com/css2?family=Fredoka:wght@400;500;600&family=Poppins:wght@400;500;600&display=swap">
<style>
:root{
  --orange:#e8552b;
  --teal:#0a93a9;
  --teal-dark:#08798c;
  --ink:#222226;
  --text:#4a4a4f;
  --muted:#9a9a9f;
  --footer:#2c2c2f;
  --footer-text:#c9c9cc;
  --white:#ffffff;
  --peach:#f6c7b6;
}
*{box-sizing:border-box;margin:0;padding:0}
html,body{width:1200px;height:4640px;overflow:hidden;background:var(--white)}
body{position:relative;font-family:"Poppins",sans-serif;color:var(--text)}
.abs{position:absolute}
.display{font-family:"Fredoka",sans-serif}

/* header */
.site-header{left:0;top:0;width:1200px;height:90px;background:var(--white)}
.brand{display:flex;align-items:center;gap:10px;color:var(--teal);font-family:"Fredoka",sans-serif;font-weight:500}
.brand-dot{width:22px;height:22px;border-radius:50%;background:var(--teal)}
.site-header .brand{left:88px;top:28px;font-size:28px}
.main-nav{left:515px;top:38px;display:flex;gap:22px;align-items:center;font-size:12.5px;font-weight:500;color:var(--ink);letter-spacing:.2px}
.our-work{left:1018px;top:0;width:182px;height:90px;background:var(--orange);color:var(--white);display:flex;align-items:center;justify-content:center;gap:8px;font-size:13px;font-weight:500}

/* hero */
.hero{left:0;top:90px;width:1200px;height:798px;background:linear-gradient(120deg,#4a3a2c 0%,#8a6a48 35%,#c79a66 60%,#e9d6b2 85%,#a98a62 100%)}
.hero-title{left:80px;top:355px;font-size:80px;line-height:80px;font-weight:500;color:var(--white)}
.hero-tabs{left:733px;top:822px;width:467px;height:66px;background:var(--white);display:flex;align-items:center;gap:38px;padding-left:45px;font-size:15px;color:var(--ink)}
.hero-tabs .active{color:var(--orange);text-decoration:underline;text-underline-offset:4px}

/* about */
.about-title{left:0;top:1000px;width:1200px;text-align:center;font-size:48px;font-weight:500;color:var(--ink)}
.about-sub{left:0;top:1062px;width:1200px;text-align:center;font-size:15px;font-weight:500;color:var(--ink)}
.about-copy{left:255px;top:1102px;width:690px;text-align:center;font-size:14px;line-height:22px}

/* story */
.story-photo{left:0;top:1274px;width:545px;height:554px;background:linear-gradient(160deg,#8b97a3 0%,#5b6470 45%,#3a3530 100%)}
.eyebrow{font-size:16px;color:var(--muted);font-weight:500}
.story-eyebrow{left:597px;top:1340px}
.story-title{left:596px;top:1368px;font-size:48px;line-height:48px;font-weight:500;color:var(--ink)}
.story-copy{left:598px;top:1480px;width:430px;font-size:14px;line-height:22px}
.btn-dark{left:597px;top:1675px;width:138px;height:44px;background:var(--ink);color:var(--white);font-size:11.5px;font-weight:600;display:flex;align-items:center;justify-content:center}

/* services */
.services-band{left:0;top:1920px;width:1200px;height:725px;background:var(--teal)}
.services-title{left:0;top:1993px;width:1200px;text-align:center;font-size:48px;font-weight:500;color:var(--white)}
.service-card{left:88px;top:2088px;width:1024px;height:694px;background:linear-gradient(180deg,#c9c6c0 0%,#aaa49b 50%,#514c46 78%,#1c1c1c 100%)}
.service-name{left:132px;top:2664px;font-size:58px;font-weight:500;color:var(--white)}
.arrow-btn{top:2685px;width:40px;height:40px;display:flex;align-items:center;justify-content:center}

/* review */
.quote-mark{left:115px;top:2890px}
.review-eyebrow{left:411px;top:2902px}
.review-title{left:411px;top:2934px;font-size:38px;font-weight:500;color:var(--ink)}
.review-copy{left:411px;top:2986px;width:550px;font-size:14.5px;line-height:22px}
.review-name{left:411px;top:3086px;font-size:16px;font-weight:600;color:var(--orange)}
.review-dots{left:1068px;top:2995px;display:flex;flex-direction:column;gap:16px}
.sq{width:10px;height:10px;background:#bdbdbd}
.sq.on{background:var(--orange)}

/* recent work */
.work-title{left:0;top:3198px;width:1200px;text-align:center;font-size:46px;font-weight:500;color:var(--ink)}
.tile{position:absolute}
.work-dots{left:578px;top:3878px;display:flex;gap:4px}

/* cta */
.cta-band{left:0;top:3962px;width:1200px;height:198px;background:linear-gradient(90deg,#e24d24,#ec6535)}
.cta-title{left:86px;top:4036px;font-size:40px;font-weight:500;color:var(--white)}
.cta-sub{left:86px;top:4090px;font-size:14px;font-weight:500;color:var(--white)}
.cta-btn{left:925px;top:4052px;width:186px;height:42px;background:var(--white);color:var(--ink);font-size:12px;font-weight:600;display:flex;align-items:center;justify-content:center}

/* footer */
.site-footer{left:0;top:4160px;width:1200px;height:480px;background:var(--footer)}
.site-footer .brand{left:130px;top:4322px;font-size:29px}
.socials{left:175px;top:4378px;display:flex;gap:10px}
.social{width:40px;height:40px;border-radius:50%;border:1.5px solid #4a4a4e}
.foot-col{top:4282px;color:var(--footer-text);font-size:11.5px;line-height:22px}
.foot-col h4{color:var(--white);font-size:15px;font-weight:500;margin-bottom:14px}
.contact-item{display:flex;gap:10px;margin-bottom:16px;line-height:17px}
.contact-item svg{flex:none;margin-top:3px}
.copyright{left:0;top:4600px;width:1200px;text-align:center;font-size:11px;color:var(--footer-text)}
.to-top{left:1136px;top:4586px;width:40px;height:40px;border-radius:50%;background:var(--orange);display:flex;align-items:center;justify-content:center}
</style>
</head>
<body>

<header class="site-header abs">
  <div class="brand abs"><span class="brand-dot"></span>Keeping Moments</div>
  <nav class="main-nav abs">
    <svg width="16" height="14" viewBox="0 0 16 14"><path d="M8 0 16 7h-2.5v7h-4V9.5h-3V14h-4V7H0z" fill="#e8552b"/></svg>
    <span>SERVICES OFFERED</span><span>ABOUT ME</span><span>CLIENT REVIEWS</span><span>CONTACT</span>
  </nav>
  <div class="our-work abs">
    <svg width="16" height="13" viewBox="0 0 16 13"><path d="M1 3h3.5L6 1h4l1.5 2H15v10H1z" fill="#fff"/><circle cx="8" cy="7.5" r="2.6" fill="#e8552b"/></svg>
    OUR WORK
  </div>
</header>

<section class="hero abs" role="img" aria-label="Bright dining room and living room with wooden floor and display shelf"></section>
<h1 class="hero-title abs display">Keeping<br>Moments<br>Photography</h1>
<div class="hero-tabs abs"><span class="active">Real estate</span><span>Sports</span><span>Digital transfers</span></div>

<h2 class="about-title abs display">About Me</h2>
<p class="about-sub abs">Keeping Moments can help meet your individual needs!</p>
<p class="about-copy abs">Lorem ipsum dolor sit amet, consectetur adipisicing elit, sed do eiusmod tempor incididunt ut labore et dolore magna aliqua. Ut enim ad minim veniam, quis nostrud exercitation ullamco laboris nisi ut aliquip ex ea commodo consequat. Duis aute..</p>

<div class="story-photo abs" role="img" aria-label="Two young women playing basketball on an outdoor court"></div>
<p class="eyebrow story-eyebrow abs">Presentation</p>
<h2 class="story-title abs display">Photographer &amp;<br>Storyteller</h2>
<p class="story-copy abs">It is a long established fact that a reader will be distracted by the readable content of a page when looking at its layout. The point of using Lorem Ipsum is that it has a more-or-less normal distribution of letters, as opposed to using 'Content here, content here', making it look like readable English. Many desktop publishing packages and web page editors now use Lorem Ipsum as their default model text, and a search for 'lorem ipsum...</p>
<div class="btn-dark abs">READ MORE</div>

<section class="services-band abs"></section>
<h2 class="services-title abs display">Our Services</h2>
<div class="service-card abs" role="img" aria-label="Home entryway with wooden cabinet, flowers, white doors and chandelier"></div>
<h3 class="service-name abs display">Real Estate</h3>
<div class="arrow-btn abs" style="left:970px;background:#c2472a"><svg width="14" height="10" viewBox="0 0 14 10"><path d="M13 5H2M5 1 1 5l4 4" stroke="#fff" stroke-width="1.4" fill="none"/></svg></div>
<div class="arrow-btn abs" style="left:1018px;background:var(--teal)"><svg width="14" height="10" viewBox="0 0 14 10"><path d="M1 5h11M9 1l4 4-4 4" stroke="#fff" stroke-width="1.4" fill="none"/></svg></div>

<svg class="quote-mark abs" width="270" height="225" viewBox="0 0 270 225" aria-hidden="true">
  <defs><linearGradient id="qg" x1="0" y1="0" x2="0" y2="1"><stop offset="0" stop-color="#f5b9a3"/><stop offset="1" stop-color="#fde9e1"/></linearGradient></defs>
  <path d="M60 5C20 40 0 90 5 150c3 45 30 70 60 70 32 0 55-25 55-55 0-30-22-52-50-52-6 0-10 1-14 2 4-40 22-75 45-100z" fill="url(#qg)"/>
  <path d="M195 5c-40 35-60 85-55 145 3 45 30 70 60 70 32 0 55-25 55-55 0-30-22-52-50-52-6 0-10 1-14 2 4-40 22-75 45-100z" fill="url(#qg)"/>
</svg>
<p class="eyebrow review-eyebrow abs">Customer Review</p>
<h2 class="review-title abs">YOUR MEMORIES MATTER</h2>
<p class="review-copy abs">It is a long established fact that a reader will be distracted by the readable content of a page when looking at its layout. The point of using Lorem Ipsum is that it has a more-or-less normal distribution of letters, as opposed to using...</p>
<p class="review-name abs">DANA ROWE</p>
<div class="review-dots abs"><span class="sq on"></span><span class="sq"></span><span class="sq"></span></div>

<h2 class="work-title abs">RECENT WORK</h2>
<div class="tile" style="left:90px;top:3268px;width:243px;height:280px;background:linear-gradient(180deg,#111,#2a1a14 60%,#111)" role="img" aria-label="Basketball player dribbling against a black background"></div>
<div class="tile" style="left:344px;top:3268px;width:243px;height:280px;background:linear-gradient(180deg,#8fa3ad,#6d7479 50%,#3e4245)" role="img" aria-label="Aerial view of city skyscrapers beside a park"></div>
<div class="tile" style="left:598px;top:3268px;width:513px;height:280px;background:linear-gradient(180deg,#13243f 0%,#1e3a5f 55%,#2f5a2a 100%)" role="img" aria-label="Two football players tackling in a stadium at night"></div>
<div class="tile" style="left:90px;top:3560px;width:497px;height:280px;background:linear-gradient(120deg,#4a3a2c,#b38a5a 50%,#e3d2b0)" role="img" aria-label="Living and dining room with leather sofa and wooden table"></div>
<div class="tile" style="left:598px;top:3560px;width:243px;height:280px;background:linear-gradient(180deg,#2a2218,#6a5434 60%,#1a1a1a)" role="img" aria-label="Two men in suits beside a car in a lit lobby"></div>
<div class="tile" style="left:860px;top:3567px;width:251px;height:273px;background:var(--teal);opacity:.85" role="img" aria-label="Luxury car parked outside a building"></div>
<div class="tile" style="left:968px;top:3680px;width:36px;height:36px;border-radius:50%;border:1.5px solid #fff;display:flex;align-items:center;justify-content:center">
  <svg width="16" height="16" viewBox="0 0 16 16"><path d="M7 9l2-2M6 6 4 8a2.1 2.1 0 0 0 3 3l1-1M10 10l2-2a2.1 2.1 0 0 0-3-3L8 6" stroke="#fff" stroke-width="1.4" fill="none"/></svg>
</div>
<div class="work-dots abs"><span class="sq"></span><span class="sq on"></span><span class="sq"></span></div>

<section class="cta-band abs"></section>
<h2 class="cta-title abs">LET KEEPING MOMENTS HELP</h2>
<p class="cta-sub abs">Call or email to set up a time to meet &amp; create a plan to meet your individual needs.</p>
<div class="cta-btn abs">REQUEST A MEETING</div>

<footer class="site-footer abs"></footer>
<div class="brand abs" style="left:130px;top:4322px;font-size:29px"><span class="brand-dot"></span>Keeping Moments</div>
<div class="socials abs">
  <span class="social" aria-label="Social profile one"></span>
  <span class="social" aria-label="Social profile two"></span>
  <span class="social" aria-label="Video channel"></span>
  <span class="social" aria-label="Photo profile"></span>
</div>
<div class="foot-col abs" style="left:467px">
  <h4>QUICK LINK</h4>
  <p>HOME</p><p>SERVICES OFFERED</p><p>ABOUT ME</p><p>CLIENT REVIEWS</p><p>CONTACT</p>
</div>
<div class="foot-col abs" style="left:660px">
  <h4>CATEGORIES</h4>
  <p>REAL ESTATE</p><p>SPORTS</p><p>DIGITAL TRANSFERS</p>
</div>
<div class="foot-col abs" style="left:852px;width:270px">
  <h4>CONTACT US</h4>
  <div class="contact-item"><svg width="12" height="9" viewBox="0 0 12 9"><rect width="12" height="9" fill="#e8552b"/><path d="M0 0l6 5 6-5" stroke="#2c2c2f" fill="none"/></svg><span>Email:<br>contact@KeepingMomentsLLC.example</span></div>
  <div class="contact-item"><svg width="12" height="12" viewBox="0 0 12 12"><path d="M2 0l3 3-1.5 1.5a7 7 0 0 0 4 4L9 7l3 3-2 2C5 12 0 7 0 2z" fill="#e8552b"/></svg><span>Appointment:<br>Hours by Appointment Only</span></div>
  <div class="contact-item"><svg width="10" height="13" viewBox="0 0 10 13"><path d="M5 0a5 5 0 0 1 5 5c0 3-5 8-5 8S0 8 0 5a5 5 0 0 1 5-5z" fill="#e8552b"/><circle cx="5" cy="5" r="1.8" fill="#2c2c2f"/></svg><span>Location:<br>Marla Hensley Keeping Moments LLC 2045 N Maple Avenue Fairview, KY 40000</span></div>
</div>
<p class="copyright abs">© Copyright 2023 &nbsp;All Right Reserveds</p>
<div class="to-top abs"><svg width="12" height="8" viewBox="0 0 12 8"><path d="M1 7l5-5 5 5" stroke="#fff" stroke-width="1.6" fill="none"/></svg></div>

</body>
</html>
```